Dental Savings Plan - Marcus Delvane DDS

We need a tri-fold brochure and 1 page flyer/poster for Dr. Marcus Delvane' dental office located on Maui, Hawaii. We are offering a new "Dental Savings Plan" to patients.
I have included 3 photos, along with the office logo. You do not have to use all photos if you do not want to. We want this to catch the eyes of patients, easy for them to read and understand, and to show them that this is a much better option than dental insurance.
Please use same Hawaiian theme and colors on the office website https://www.pearlreefcare.com .

Please also include the following to promote this new plan:

Dental Services Include
• Professional Dental Cleanings (2 per benefit year)
• Perio Maintenance Cleanings (3 per benefit year) covered at 80%
• Radiographs as needed (1 set of X-rays per benefit year)
• Doctor Examinations (2 per benefit year)
• Ozone Treatment
• KOROV Amalgam Removal
• Additional limited/emergency exam (1 per benefit year)
• Cosmetic consultation
• 15% discount on all other services (including cosmetic procedures)
• 10% discount on implants and implant crowns

Advantages of the Dental Savings Plan
1. No deductibles
2. No waiting periods
3. No claims to file
4. No frequency limitations or exclusions
5. No yearly maximum benefits
6. No pre-authorization requirements
7. No pre-existing conditions limitations
8. State of the art facility and technology
9. Immediate enrollment
10. Highest quality of care for you and your Ohana

Annual Fee
$399 first family member/individual (equivalent to $33 per month)
$349 second family member (equivalent to $29 per month)
$249 each additional family member (equivalent to $20 per month)

Provisions of the Dental Savings Plan
• May not be combined with insurance plans, discounts or promotions
• This Dental Savings Plan is not an insurance plan, but a payment arrangement provided by Marcus Delvane DDS, and is not transferable to any other dental office or dental specialist
• Payment for services are due at the date of service
• This program is for you and is not transferable
• Benefits are provided for one year from the date the plan is purchased
• Must be paid in full when starting the plan
• No refunds will be provided for dues of the plan annual fee under any circumstances, including failure to schedule and maintain appointments
• If Paxwel Fund is used to pay for the program and for services then only a 10% discount will be given
• To receive the full 15% discount on restorative treatment, you must schedule the appointment the day it is recommended. Any failed appointment results in the loss of the 15% discount.

Target Market(s)

Dental patients without dental insurance

Industry/Entity Type

Dental Clinic

Requirements
Must have
• My project must have the logo file to identify the dental office, Hawaiian theme, same colors as website, match style of website font, theme and colors, as well as, all the Dental Services, Advantages of the Dental Savings Plan, Annual Fee, and the Provisions of the Dental Savings Plan.

```html
<!DOCTYPE html>
<html lang="en">
<head>
<meta charset="utf-8">
<title>Dental Savings Plan – Marcus Delvane DDS</title>
<link rel="stylesheet" href="https://fonts.googleapis.com/css2?family=Arvo:wght@700&family=Fira+Sans+Condensed:ital,wght@0,400;0,500;1,600;1,700&display=swap">
<style>
  :root{
    --reef-blue:#22a7e0;
    --heading-blue:#2aa9e6;
    --lava:#2d2f2e;
    --paper:#ffffff;
    --stage:#e4e4e4;
    --label-glass:rgba(70,110,140,.72);
    --label-ink:#f4f4f4;
    --cover-top:#4d9bd8;
    --cover-bottom:#17aecf;
    --fee-photo-a:#eee0d9;
    --fee-photo-b:#e4e7ea;
    --dentist-photo-a:#e6e9eb;
    --dentist-photo-b:#4d6782;
  }
  *{margin:0;padding:0;box-sizing:border-box}
  html,body{width:1200px;height:1036px;overflow:hidden}
  body{background:var(--stage);font-family:"Fira Sans Condensed",sans-serif;color:var(--paper);position:relative}

  .spread{position:absolute;left:30px;width:1140px;height:480px;display:flex;box-shadow:0 6px 18px rgba(0,0,0,.18)}
  .spread--outside{top:24px}
  .spread--inside{top:532px}
  .panel{position:relative;width:380px;height:480px;overflow:hidden}
  .panel--lava{background:var(--lava)}
  .panel--reef{background:var(--reef-blue)}

  .photo{position:absolute;left:0;width:100%}

  /* fee panel */
  .fee-photo{top:0;height:150px;background:linear-gradient(120deg,var(--fee-photo-a),var(--fee-photo-b))}
  .fee-body{position:absolute;top:150px;left:0;right:0;bottom:0;padding:26px 34px}
  .fee-title{font-style:italic;font-weight:700;font-size:38px;color:var(--heading-blue);margin-bottom:18px}
  .fee-item{margin-bottom:20px;font-size:17px;line-height:1.3}
  .fee-item strong{font-weight:700;font-style:italic;font-size:21px}
  .fee-item .eq{display:block;font-size:15px}

  /* contact panel */
  .social{position:absolute;top:34px;left:0;right:0;display:flex;justify-content:center;align-items:center;gap:16px}
  .social-link{display:flex;align-items:center;gap:5px;font-size:13px;font-weight:500;color:var(--paper)}
  .social-square{width:8px;height:8px;background:var(--paper)}
  .social-pin{width:24px;height:24px;border:2px solid var(--paper);border-radius:3px;display:flex;align-items:center;justify-content:center}
  .dentist-photo{top:92px;height:200px;background:linear-gradient(110deg,var(--dentist-photo-a),var(--dentist-photo-b))}
  .contact{position:absolute;top:318px;left:34px;right:20px}
  .contact-title{font-style:italic;font-weight:700;font-size:27px;margin-bottom:12px}
  .contact-row{display:flex;align-items:center;gap:9px;font-size:15.5px;margin-bottom:7px}
  .contact-row svg{flex:none}

  /* cover panel */
  .cover-photo{top:0;height:100%;background:linear-gradient(180deg,var(--cover-top),var(--cover-bottom))}
  .cover-label{position:absolute;top:60px;right:26px;width:190px;padding:14px 22px;border-radius:14px;background:var(--label-glass);font-family:"Arvo",serif;font-weight:700;font-size:27px;line-height:.95;color:var(--label-ink)}

  /* inside panels */
  .inside-body{position:absolute;top:26px;left:22px;right:18px}
  .inside-title{font-style:italic;font-weight:600;font-size:23px;line-height:1.15;margin-bottom:14px}
  .service-list,.provision-list{list-style:none}
  .service-list li{position:relative;padding-left:10px;font-size:12.5px;line-height:1.22;margin-bottom:9px}
  .service-list li::before,.provision-list li::before{content:"•";position:absolute;left:0}
  .advantage-list{list-style:none;padding-left:4px}
  .advantage-list li{font-size:12.5px;line-height:1.3;margin-bottom:12px;display:flex;gap:8px}
  .advantage-list .num{min-width:12px}
  .provision-list li{position:relative;padding-left:10px;font-size:11px;line-height:1.2;margin-bottom:10px}
  .panel-badge{position:absolute;bottom:18px;left:50%;transform:translateX(-50%);width:46px;height:46px;border-radius:50%}
  .panel-badge--fill{background:var(--reef-blue)}
  .panel-badge--line{border:2px solid var(--paper)}
</style>
</head>
<body>

<section class="spread spread--outside" aria-label="Brochure outside">
  <article class="panel panel--lava fee-panel">
    <div class="photo fee-photo" role="img" aria-label="Photo of a patient smiling during a dental exam"></div>
    <div class="fee-body">
      <h2 class="fee-title">Annual Fee</h2>
      <p class="fee-item"><strong>$399</strong> first family member/individual<span class="eq">(equivalent to $33 per month)</span></p>
      <p class="fee-item"><strong>$349</strong> second family member<span class="eq">(equivalent to $29 per month)</span></p>
      <p class="fee-item"><strong>$249</strong> each additional family member<span class="eq">(equivalent to $20 per month)</span></p>
    </div>
  </article>

  <article class="panel panel--reef contact-panel">
    <div class="social" aria-label="Social links">
      <span class="social-link"><span class="social-square"></span>Chirply</span>
      <span class="social-link"><span class="social-square"></span>Ohanabook</span>
      <span class="social-pin">
        <svg width="12" height="14" viewBox="0 0 12 14"><path d="M6 13s5-5 5-8A5 5 0 0 0 1 5c0 3 5 8 5 8z" fill="none" stroke="#fff" stroke-width="1.6"/><circle cx="6" cy="5" r="1.6" fill="#fff"/></svg>
      </span>
    </div>
    <div class="photo dentist-photo" role="img" aria-label="Photo of the dentist beside an X-ray monitor"></div>
    <div class="contact">
      <h2 class="contact-title">Contact Us:</h2>
      <p class="contact-row"><svg width="16" height="16" viewBox="0 0 16 16"><circle cx="8" cy="8" r="7" fill="none" stroke="#fff" stroke-width="1.2"/><path d="M5.5 4.5l1.5 1.6-.8 1c.6 1.2 1.3 1.9 2.5 2.5l1-.8 1.6 1.5-1 1.2C7.7 11.3 4.7 8.3 4.5 5.5z" fill="#fff"/></svg>808-555-0172</p>
      <p class="contact-row"><svg width="16" height="16" viewBox="0 0 16 16"><circle cx="8" cy="8" r="7" fill="none" stroke="#fff" stroke-width="1.2"/><rect x="4.2" y="5.5" width="7.6" height="5" fill="none" stroke="#fff" stroke-width="1"/><path d="M4.2 5.5L8 8.4l3.8-2.9" fill="none" stroke="#fff" stroke-width="1"/></svg>hello@pearlreefcare.com</p>
      <p class="contact-row"><svg width="16" height="16" viewBox="0 0 16 16"><circle cx="8" cy="8" r="7" fill="none" stroke="#fff" stroke-width="1.2"/><circle cx="8" cy="8" r="3.8" fill="none" stroke="#fff" stroke-width="1"/><path d="M4.2 8h7.6M8 4.2v7.6" stroke="#fff" stroke-width="1"/></svg>www.pearlreefcare.com</p>
      <p class="contact-row"><svg width="16" height="16" viewBox="0 0 16 16"><circle cx="8" cy="8" r="7" fill="none" stroke="#fff" stroke-width="1.2"/><path d="M8 12s3-3 3-5a3 3 0 0 0-6 0c0 2 3 5 3 5z" fill="#fff"/></svg>4470 Palena Way # 12, Kihei, HI 96753</p>
    </div>
  </article>

  <article class="panel cover-panel">
    <div class="photo cover-photo" role="img" aria-label="Photo of a palm tree over a turquoise Hawaiian bay"></div>
    <h1 class="cover-label">Dental<br>Savings<br>Plan</h1>
  </article>
</section>

<section class="spread spread--inside" aria-label="Brochure inside">
  <article class="panel panel--lava">
    <div class="inside-body">
      <h2 class="inside-title">Dental Services Include</h2>
      <ul class="service-list">
        <li>Professional Dental Cleanings<br>(2 per benefit year)</li>
        <li>Perio Maintenance Cleanings<br>(3 per benefit year) covered at 80%</li>
        <li>Radiographs as needed<br>(1 set of X-rays per benefit year)</li>
        <li>Doctor Examinations<br>(2 per benefit year)</li>
        <li>Ozone Treatment</li>
        <li>KOROV Amalgam Removal</li>
        <li>Additional limited/emergency exam<br>(1 per benefit year)</li>
        <li>Cosmetic consultation</li>
        <li>15% discount on all other services<br>(including cosmetic procedures)</li>
        <li>10% discount on implants and implant crowns</li>
      </ul>
    </div>
    <span class="panel-badge panel-badge--fill"></span>
  </article>

  <article class="panel panel--reef">
    <div class="inside-body">
      <h2 class="inside-title">Advantages of the<br>Dental Savings Plan</h2>
      <ol class="advantage-list">
        <li><span class="num">1.</span>No deductibles</li>
        <li><span class="num">2.</span>No waiting periods</li>
        <li><span class="num">3.</span>No claims to file</li>
        <li><span class="num">4.</span>No frequency limitations or exclusions</li>
        <li><span class="num">5.</span>No yearly maximum benefits</li>
        <li><span class="num">6.</span>No pre-authorization requirements</li>
        <li><span class="num">7.</span>No pre-existing conditions limitations</li>
        <li><span class="num">8.</span>State of the art facility and technology</li>
        <li><span class="num">9.</span>Immediate enrollment</li>
        <li><span class="num">10.</span>Highest quality of care for you<br>and your Ohana</li>
      </ol>
    </div>
    <span class="panel-badge panel-badge--line"></span>
  </article>

  <article class="panel panel--lava">
    <div class="inside-body">
      <h2 class="inside-title">Provisions of the<br>Dental Savings Plan</h2>
      <ul class="provision-list">
        <li>May not be combined with insurance plans, discounts or promotions</li>
        <li>This Dental Savings Plan is not an insurance plan, but a payment arrangement provided by Marcus Delvane DDS, and is not transferable to any other dental office or dental specialist</li>
        <li>Payment for services are due at the date of service</li>
        <li>This program is for you and is not transferable</li>
        <li>Benefits are provided for one year from the date the plan is purchased</li>
        <li>Must be paid in full when starting the plan</li>
        <li>No refunds will be provided for dues of the plan annual fee under any circumstances, including failure to schedule and maintain appointments</li>
        <li>If Paxwel Fund is used to pay for the program and for services then only a 10% discount will be given</li>
        <li>To receive the full 15% discount on restorative treatment, you must schedule the appointment the day it is recommended. Any failed appointment results in the loss of the 15% discount.</li>
      </ul>
    </div>
    <span class="panel-badge panel-badge--fill"></span>
  </article>
</section>

</body>
</html>
```